We need a Chatterbox ad design for mobile app business.

"LUMAVO" app platform providing a range of services like home massage therapy or home hair cut needs 4 Chatterbox advertisement designs to hire the service providers. Each ad needs to bold one the professions and also show the others professions!! let say we we need one design emphasizing on Massage Therapist, one for hair stylists, one for tune up technicians, and that includes 4 professions : house keepers + lawn mowers, snow blowers and tutors. Each one of the designs requires a different content.
This app is gonna lunch in Thunder Bay/ON/Canada, So it is necessary to be mentioned. And even a design must be included the pandemic situation for some professions and EARNING A SIDE INCOME UP TO 50K PER YEAR AND ALSO TO BE YOUR OWN BOSS!.
Lumavo is service application that provides different ranges of services like automotive service, home cleaning, massage therapy and etc. So the design must be a very nice combination of services and very clear.

To get better understanding of the app please check it in the quindel market store or brisk store through following links:
https://apps.quindelmarket.example/details?id=com.lumavojobs

Requirements
Nice to have
• Apply green, silver and golden colors

```html
<!DOCTYPE html>
<html lang="en">
<head>
<meta charset="utf-8">
<title>Lumavo – Professional Massage Therapist Ad</title>
<link rel="stylesheet" href="https://fonts.googleapis.com/css2?family=Montserrat:wght@300;400;600;700;800;900&display=swap">
<style>
  :root{
    --green-dark:#127a2a;
    --green-mid:#0f9a2f;
    --green-bright:#14c53a;
    --gold:#b8903a;
    --gold-light:#f3dc92;
    --black:#050505;
    --white:#ffffff;
    --ink:#0b0b0b;
  }
  *{margin:0;padding:0;box-sizing:border-box}
  html,body{width:1200px;height:1200px;overflow:hidden;background:var(--white)}
  .ad{position:relative;width:1200px;height:1200px;overflow:hidden;font-family:"Montserrat",sans-serif;background:var(--white)}
  .ad-shapes{position:absolute;inset:0}
  .brand{position:absolute;left:78px;top:258px;display:flex;align-items:center;gap:14px}
  .brand-dot{width:36px;height:36px;border-radius:50%;border:6px solid var(--green-mid)}
  .brand-name{font-weight:800;font-size:62px;color:var(--green-mid);letter-spacing:1px;line-height:1}

  .other-jobs{position:absolute;left:80px;top:345px;width:350px}
  .other-jobs-title{font-weight:800;font-size:17px;letter-spacing:3px;color:var(--green-dark);margin-bottom:10px}
  .other-jobs-list{list-style:none;display:grid;grid-template-columns:1fr 1fr;column-gap:14px;row-gap:7px}
  .other-jobs-list li{display:flex;align-items:center;gap:7px;font-weight:600;font-size:14.5px;color:var(--ink);white-space:nowrap}
  .other-jobs-list li::before{content:"";width:9px;height:9px;border-radius:50%;background:var(--green-bright);border:2px solid var(--gold);flex:none}

  .headline-kicker{position:absolute;left:63px;top:684px;font-weight:300;font-size:48px;letter-spacing:14px;color:var(--ink);line-height:1}
  .headline-main{position:absolute;left:60px;top:738px;font-weight:900;font-size:104px;line-height:94px;color:var(--white)}
  .headline-line{display:block}
  .headline-line-massage{letter-spacing:0}
  .headline-line-therapist{letter-spacing:-4px}
  .home-pill{position:absolute;left:43px;top:933px;width:626px;height:82px;border-radius:41px;
    background:linear-gradient(180deg,#8f6a22 0%,var(--gold-light) 35%,#c89f45 65%,#8a6520 100%);
    display:flex;align-items:center;justify-content:center;font-weight:900;font-size:68px;color:var(--ink);letter-spacing:-1px}
  .book-btn{position:absolute;left:207px;top:1056px;width:292px;height:58px;border-radius:29px;background:var(--black);
    border:4px solid var(--gold);display:flex;align-items:center;justify-content:center;font-weight:900;font-size:35px;color:var(--white);letter-spacing:1px}
  .download{position:absolute;left:87px;top:1144px;font-size:23px;font-weight:400;color:var(--white)}
  .store{position:absolute;top:1134px;height:40px;display:flex;align-items:center;gap:8px;color:var(--white);font-weight:600;font-size:16px}
  .store-brisk{left:408px}
  .store-quindel{left:536px;padding:0 10px;border:1px solid #8a8a8a;border-radius:6px}
  .store-mark{width:14px;height:14px;background:var(--white);border-radius:2px}
  .launch{position:absolute;left:720px;top:800px;width:420px;text-align:center;font-weight:800;font-size:29px;line-height:39px;color:var(--white)}
  .income-box{position:absolute;left:778px;top:940px;width:310px;height:260px;border-radius:22px 22px 0 0;
    background:linear-gradient(180deg,#b48c38 0%,var(--gold-light) 30%,#c9a14b 60%,#a9812f 100%);
    display:flex;align-items:center;justify-content:center;text-align:center;padding:6px 10px 0;
    font-weight:900;font-size:23px;line-height:33px;color:var(--ink)}
</style>
</head>
<body>
<main class="ad">
  <svg class="ad-shapes" width="1200" height="1200" viewBox="0 0 1200 1200">
    <defs>
      <linearGradient id="band-green" x1="0" y1="0" x2="0" y2="1">
        <stop offset="0" stop-color="#127a2a"/>
        <stop offset="0.35" stop-color="#14c53a"/>
        <stop offset="0.55" stop-color="#14c53a"/>
        <stop offset="0.75" stop-color="#127a2a"/>
        <stop offset="1" stop-color="#127a2a"/>
      </linearGradient>
      <linearGradient id="ring-green" x1="0" y1="0" x2="1" y2="1">
        <stop offset="0" stop-color="#14c53a"/>
        <stop offset="0.4" stop-color="#127a2a"/>
        <stop offset="0.7" stop-color="#14c53a"/>
        <stop offset="1" stop-color="#14c53a"/>
      </linearGradient>
      <linearGradient id="gold-line" x1="0" y1="0" x2="1" y2="1">
        <stop offset="0" stop-color="#f3dc92"/>
        <stop offset="0.5" stop-color="#b8903a"/>
        <stop offset="1" stop-color="#c9a14b"/>
      </linearGradient>
      <linearGradient id="photo-tone" x1="0" y1="0" x2="1" y2="1">
        <stop offset="0" stop-color="#eef0f3"/>
        <stop offset="0.5" stop-color="#e2c0a8"/>
        <stop offset="1" stop-color="#f1ece8"/>
      </linearGradient>
      <linearGradient id="black-band" x1="0" y1="0" x2="0" y2="1">
        <stop offset="0" stop-color="#2a2a2a"/>
        <stop offset="0.3" stop-color="#050505"/>
      </linearGradient>
    </defs>

    <rect class="band-green" x="0" y="634" width="1200" height="451" fill="url(#band-green)"/>
    <rect class="band-green-top" x="0" y="603" width="600" height="20" fill="#127a2a"/>
    <rect class="gold-rule" x="0" y="623" width="1200" height="11" fill="#b8903a"/>
    <rect class="gold-rule" x="0" y="1085" width="1200" height="9" fill="#b8903a"/>
    <rect class="band-black" x="0" y="1093" width="1200" height="107" fill="url(#black-band)"/>

    <rect class="accent-pill" x="186" y="549" width="220" height="52" rx="26" fill="#14c53a" stroke="#b8903a" stroke-width="8"/>
    <rect class="accent-pill" x="415" y="466" width="160" height="53" rx="26" fill="#14c53a" stroke="#b8903a" stroke-width="8"/>
    <rect class="accent-pill" x="463" y="549" width="160" height="52" rx="26" fill="#14c53a" stroke="#b8903a" stroke-width="8"/>

    <circle class="ring-gold" cx="960" cy="274" r="512" fill="url(#gold-line)"/>
    <circle class="ring-green" cx="960" cy="274" r="502" fill="url(#ring-green)"/>
    <circle class="ring-white" cx="960" cy="274" r="442" fill="#ffffff"/>
    <circle class="photo-area" cx="960" cy="274" r="434" fill="url(#photo-tone)" role="img" aria-label="Photo of a woman relaxing on a table while receiving a back massage"/>
  </svg>

  <div class="brand">
    <span class="brand-dot"></span>
    <span class="brand-name">LUMAVO</span>
  </div>

  <section class="other-jobs">
    <p class="other-jobs-title">ALSO HIRING</p>
    <ul class="other-jobs-list">
      <li>Hair Stylists</li>
      <li>Tune-up Technicians</li>
      <li>House Keepers</li>
      <li>Lawn Mowers</li>
      <li>Snow Blowers</li>
      <li>Tutors</li>
    </ul>
  </section>

  <p class="headline-kicker">PROFESSIONAL</p>
  <h1 class="headline-main"><span class="headline-line headline-line-massage">MASSAGE</span><span class="headline-line headline-line-therapist">THERAPIST</span></h1>
  <div class="home-pill">AT YOUR HOME</div>

  <div class="book-btn">BOOK NOW</div>
  <p class="download">Download the app now</p>
  <div class="store store-brisk"><span class="store-mark"></span>Brisk Store</div>
  <div class="store store-quindel">Quindel Market</div>

  <p class="launch">This app is gonna<br>lunch in<br>Thunder Bay/ON/Canada</p>

  <div class="income-box">EARNING A SIDE<br>INCOME UP TO<br>50K PER YEAR<br>AND ALSO TO<br>BE YOUR OWN<br>BOSS!</div>
</main>
</body>
</html>
```